trading data display webpage

We have build a rough wireframe of the two webpages that we want to display .The two wireframes are attached as a pdf document.
there will be login page. after login , the user will see the index page. that is the first page of the wireframe.

what we are displaying is essentially spread data. we are taking the difference in prices are two places and displaying the data. some calculations are done and is shown in the grid.

below the grid we show the behaviour on a graph. we will use bubble chart. I did not find a sample, hence have thrown in a placeholder.

this is time series data ( changes daily) and hence we need to check the behaviour.

the second wire frame shows how the user will choose the source price points and the destination price points.
we are talking here of natural gas prices hence the reference to source prices and destination prices.

you need to design the page/ pages such that the end-user loves it and is easy to use. the intent here is easy to use and easy to understand.
this will be responsive webpage since the end user will check it out on a tablet or a smartphone.

so if possible tell us how the navigation bar, the button bar, etc should fall when the screen size decreases.

I have uploaded 2 files. one is the wireframe ( pdf document) and second is the logo file.

please also let us know where to place the logo.

Target Market(s)

the target market is traders and data analyst

Industry/Entity Type

Build

Colors

Designer to choose colors to be used in the design.

Requirements
Must have
• 1. design for the web.
2. but think how the design will look when the screen size decreases.
3. tell if possible what screen components to keep and what to hide.

```html
<!DOCTYPE html>
<html lang="en">
<head>
<meta charset="utf-8">
<title>Gasline Trading – Spread Dashboard</title>
<link rel="stylesheet" href="https://fonts.googleapis.com/css2?family=Roboto:wght@300;400;500;700&family=Roboto+Condensed:wght@400;700&display=swap">
<style>
:root{
  --navy:#254d73;
  --navy-dark:#1d3f60;
  --cream:#f3ede3;
  --white:#ffffff;
  --orange:#f26522;
  --name-orange:#f26b2a;
  --link-grey:#c9d3dd;
  --green:#8ccc3c;
  --green-dark:#74b52a;
  --tab-dark:#2b2b2b;
  --row-bg:#f7f7f7;
  --line:#e1e1e1;
  --muted:#b5b5b5;
  --title-grey:#7a7a7a;
  --pie-orange:#fe9600;
  --pie-navy:#0f2541;
  --pie-teal:#007f7e;
  --pie-yellow:#ffff00;
}
*{box-sizing:border-box;margin:0;padding:0}
html,body{width:1200px;height:965px;overflow:hidden}
body{position:relative;background:var(--cream);font-family:"Roboto",sans-serif;color:#333}
.abs{position:absolute}

/* header */
.site-header{position:absolute;left:0;top:0;width:1200px;height:92px;background:var(--navy)}
.brand{display:flex;align-items:center;gap:7px;color:var(--white);font-weight:500;font-size:17px}
.brand--header{position:absolute;left:209px;top:31px}
.brand__dot{width:20px;height:20px;border-radius:50%;background:var(--green);flex:none}
.main-nav{position:absolute;top:30px;left:433px;display:flex}
.main-nav a{display:block;height:26px;line-height:26px;font-size:13px;color:var(--white);text-decoration:none;font-weight:400}
.main-nav .is-active{background:var(--orange);border-radius:3px;padding:0 13px;margin-right:24px}
.main-nav a+a{margin-right:37px}
.user{position:absolute;left:821px;top:23px;display:flex;gap:7px}
.user__avatar{width:46px;height:46px;border:2px solid #12304c;background:#d8d8d8;position:relative;overflow:hidden}
.user__avatar svg{position:absolute;left:0;top:0}
.user__name{color:var(--name-orange);font-size:13px;margin-top:3px}
.user__links{color:var(--link-grey);font-size:13px;margin-top:9px}

/* tabs */
.region-tab{position:absolute;top:155px;width:117px;height:33px;line-height:36px;text-align:center;color:var(--white);font-size:16px;font-weight:400}
.region-tab--active{background:var(--navy)}
.region-tab--idle{background:var(--tab-dark)}

/* panel */
.panel{position:absolute;left:198px;top:188px;width:804px;height:648px;background:var(--white);border:1px solid #e6e2da}
.select{position:absolute;top:226px;width:194px;height:28px;background:#f4f4f4;border:1px solid #e3e3e3;border-top:2px solid #e0e0e0;font-size:12.5px;color:#a8a8a8;font-weight:300;padding:6px 10px}
.select::after{content:"";position:absolute;right:10px;top:11px;border:5px solid transparent;border-top:5px solid var(--navy-dark)}
.chip{position:absolute;top:278px;height:28px;line-height:28px;text-align:center;background:var(--green);border-bottom:2px solid var(--green-dark);border-radius:3px;color:var(--white);font-size:13px;font-weight:300}

/* table */
.spread-table{position:absolute;left:223px;top:327px;width:755px;border-collapse:collapse;font-family:"Roboto Condensed",sans-serif}
.spread-table th{height:34px;background:var(--navy);color:var(--white);font-size:13px;font-weight:700;border-left:1px solid #e6e6e6}
.spread-table th:first-child{border-left:none;border-radius:4px 0 0 0}
.spread-table th:last-child{border-radius:0 4px 0 0}
.spread-table td{background:var(--row-bg);border:1px solid var(--line);font-family:"Roboto",sans-serif;font-size:12px;color:var(--muted);font-weight:300;text-align:center;vertical-align:middle}
.spread-table tr.row-first td{height:53px;vertical-align:bottom;padding-bottom:6px}

.chart-title{position:absolute;font-family:"Roboto Condensed",sans-serif;font-size:13px;font-weight:700;color:var(--title-grey)}

/* footer */
.site-footer{position:absolute;left:0;top:887px;width:1200px;height:78px;background:var(--navy)}
.brand--footer{position:absolute;left:262px;top:922px;gap:6px;font-size:13px;font-weight:300}
.footer-nav{position:absolute;top:924px;color:var(--white);font-size:13px;font-weight:400}
</style>
</head>
<body>

<header class="site-header">
  <div class="brand brand--header"><span class="brand__dot"></span>Gasline</div>
  <nav class="main-nav">
    <a class="is-active" href="#">Home</a>
    <a href="#">About</a>
    <a href="#">Sitemap</a>
    <a href="#">Contact Us</a>
  </nav>
  <div class="user">
    <div class="user__avatar">
      <svg width="42" height="42" viewBox="0 0 42 42"><circle cx="21" cy="15" r="8" fill="#fff"/><path d="M6 42c0-10 7-15 15-15s15 5 15 15z" fill="#fff"/></svg>
    </div>
    <div>
      <div class="user__name">Daniel Reyes</div>
      <div class="user__links">My dashboard | Logout</div>
    </div>
  </div>
</header>

<div class="region-tab region-tab--active" style="left:212px">East</div>
<div class="region-tab region-tab--idle" style="left:338px">Central</div>
<div class="region-tab region-tab--idle" style="left:463px">West</div>

<main class="panel"></main>

<div class="select" style="left:227px">Source Indices</div>
<div class="select" style="left:782px">Destination Indices</div>

<div class="chip" style="left:227px;width:59px">5 Days</div>
<div class="chip" style="left:295px;width:59px">7 Days</div>
<div class="chip" style="left:363px;width:58px">18 Days</div>
<div class="chip" style="left:536px;width:58px">Month</div>
<div class="chip" style="left:603px;width:59px">Year</div>

<table class="spread-table">
  <colgroup>
    <col style="width:127px"><col style="width:95px"><col style="width:89px"><col style="width:102px"><col style="width:113px"><col style="width:101px"><col style="width:128px">
  </colgroup>
  <thead>
    <tr><th>Spread Name</th><th>avg sprd</th><th>+ve prob</th><th>-ve prob</th><th>spike prob</th><th>avg supply</th><th>supply cut_prob</th></tr>
  </thead>
  <tbody>
    <tr class="row-first"><td>Spread 1</td><td></td><td></td><td></td><td></td><td></td><td></td></tr>
    <tr style="height:39px"><td>Spread 2</td><td></td><td></td><td></td><td></td><td></td><td></td></tr>
    <tr style="height:37px"><td>Spread 3</td><td></td><td></td><td></td><td></td><td></td><td></td></tr>
    <tr style="height:36px"><td>Spread 4</td><td></td><td></td><td></td><td></td><td></td><td></td></tr>
    <tr style="height:41px"><td>Spread 5</td><td></td><td></td><td></td><td></td><td></td><td></td></tr>
  </tbody>
</table>

<div class="chart-title" style="left:371px;top:595px">Spread vs&nbsp; Supply</div>
<svg class="abs" style="left:321px;top:617px" width="200" height="200" viewBox="0 0 200 200" role="img" aria-label="Pie chart of spread versus supply">
  <path d="M100 100L100 6A94 94 0 0 1 193.9 103.3Z" fill="var(--pie-orange)"/>
  <path d="M100 100L193.9 103.3A94 94 0 0 1 187.1 135.2Z" fill="var(--pie-navy)"/>
  <path d="M100 100L187.1 135.2A94 94 0 1 1 82.1 7.7Z" fill="var(--pie-teal)"/>
  <path d="M100 100L82.1 7.7A94 94 0 0 1 100 6Z" fill="var(--pie-yellow)"/>
</svg>

<div class="chart-title" style="left:746px;top:597px">Spread across time</div>
<svg class="abs" style="left:720px;top:620px" width="200" height="185" viewBox="720 620 200 185" role="img" aria-label="Bar chart of spread across time" font-family="Arial, sans-serif">
  <g fill="#000" font-size="6" text-anchor="end">
    <text x="737" y="635">40</text><text x="737" y="655">35</text><text x="737" y="674">30</text>
    <text x="737" y="694">25</text><text x="737" y="713">20</text><text x="737" y="733">15</text>
    <text x="737" y="752">10</text><text x="737" y="772">5</text><text x="738" y="787" font-size="11">0</text>
  </g>
  <rect x="746" y="652" width="25" height="131" fill="#f0282c"/>
  <rect x="774" y="671" width="24" height="112" fill="#f57c00"/>
  <rect x="801" y="749" width="25" height="34" fill="#fde74c"/>
  <rect x="828" y="690" width="25" height="93" fill="#72d113"/>
  <rect x="855" y="634" width="24" height="149" fill="#76a3d6"/>
  <rect x="881" y="771" width="25" height="12" fill="#5a3464"/>
  <path d="M743 628V783H911" stroke="#222" stroke-width="1.6" fill="none"/>
  <g fill="#000" font-size="6" text-anchor="middle">
    <text x="759" y="793">Apple</text><text x="786" y="793">Orange</text><text x="813" y="793">Banana</text>
    <text x="840" y="793">Kiwifruit</text><text x="867" y="793">Blue</text><text x="867" y="800">berry</text><text x="894" y="793">Grapes</text>
  </g>
</svg>

<footer class="site-footer"></footer>
<div class="brand brand--footer"><span class="brand__dot"></span>Copyright © 2014 Gasline Trading</div>
<div class="footer-nav" style="left:716px">Home</div>
<div class="footer-nav" style="left:786px">About</div>
<div class="footer-nav" style="left:855px">Sitemap</div>
<div class="footer-nav" style="left:938px">Contact Us</div>

</body>
</html>
```